OTV Web Design Project

I'm looking for a small, friendly,functional, information based website. If you go through the attachments, you would know the nature of the business.
Updates

Hi,

I have uploaded a picture of the CEO, Mr. Darvesh Kolhi NAMPQ member. Please feel free to use it whereever appropriate.

Thanks!

Hello, I have uploaded some references. I like the colours used on the bar and would w

Example of a we page . I like this layout for the inside pages.

I am changing the tabs on my website to:

Home
About us
Services
Contact us

The services tab will have three sub pages:

Immigration
Education
AccommodationAccommodation

Target Market(s)

Young international students willing to come to Canada to study, young international students willing to immigrate to Canada, parents of the students

Industry/Entity Type

Business

Requirements
Must have
• OTV HOME
ABOUT US
CONTACT
SERVICES
TAG LINE

The website should look n feel trendy, smart, current, factual, trustworthy etc....
Nice to have
• I am looking for a bold, attractive, eye catchy home page with less text! Something that makes a statement....
Should not have
• No Clip art, flash animation, no bells n whistles please

```html
<!DOCTYPE html>
<html lang="en">
<head>
<meta charset="utf-8">
<title>OTV – Dare to Dream Canadian</title>
<link href="https://fonts.googleapis.com/css2?family=Quicksand:wght@500;600;700&display=swap" rel="stylesheet">
<style>
  :root {
    --ink: #1c1c1c;
    --muted: #9a9a9a;
    --accent: #e01b1b;
    --white: #ffffff;
    --rule: #e6e6e6;
    --bar-top: #f4f4f4;
    --bar-bottom: #bdbdbd;
    --sky-top: #b9a6d6;
    --sky-mid: #f3b15c;
    --city: #c8321a;
    --glow: #f5a13a;
  }
  * { box-sizing: border-box; margin: 0; padding: 0; }
  html, body { width: 1200px; height: 531px; overflow: hidden; background: var(--white); }
  body { position: relative; font-family: "Quicksand", sans-serif; color: var(--ink); }

  .site-header { position: absolute; left: 0; top: 0; width: 1200px; height: 69px; background: var(--white); }
  .brand { position: absolute; left: 306px; top: 20px; display: flex; align-items: center; gap: 8px;
    font-weight: 700; font-size: 30px; color: var(--ink); letter-spacing: 1px; }
  .brand-mark { width: 16px; height: 16px; background: var(--accent); }

  .main-nav { position: absolute; top: 30px; left: 452px; display: flex; align-items: center; font-size: 10.5px; font-weight: 600; }
  .main-nav a { color: var(--ink); text-decoration: none; position: absolute; white-space: nowrap; }
  .nav-home { left: 2px; top: -3px; }
  .nav-about { left: 60px; }
  .nav-services { left: 131px; }
  .nav-services svg { position: absolute; left: 32px; top: 14px; }
  .nav-contact { left: 199px; color: var(--accent) !important; border-bottom: 1px solid var(--accent); }

  .social { position: absolute; left: 822px; top: 31px; display: flex; gap: 8px; align-items: center;
    font-size: 9px; color: var(--muted); font-weight: 600; }
  .social .sep { width: 1px; height: 11px; background: var(--rule); }

  .hero { position: absolute; left: 0; top: 69px; width: 1200px; height: 313px;
    background:
      linear-gradient(180deg, rgba(255,255,255,0) 72%, var(--white) 100%),
      linear-gradient(180deg, var(--sky-top) 0%, var(--sky-mid) 38%, var(--glow) 55%, var(--city) 70%, #e9866a 85%, #f4d6cc 100%); }

  .tagline { position: absolute; left: 311px; top: 236px; color: var(--white); font-weight: 700; line-height: 0.8;
    letter-spacing: -0.5px; }
  .tagline span { display: block; }
  .tagline .line-one { font-size: 42px; }
  .tagline .line-two { font-size: 48px; }

  .service-bar { position: absolute; left: 417px; top: 367px; width: 363px; height: 44px; border-radius: 8px;
    background: linear-gradient(180deg, var(--bar-top), var(--bar-bottom));
    box-shadow: 0 0 0 3px rgba(230,230,230,0.9), 0 2px 4px rgba(0,0,0,0.15);
    display: flex; }
  .service { display: flex; align-items: center; gap: 8px; padding-left: 14px; font-size: 6.5px; font-weight: 700;
    text-transform: uppercase; color: var(--ink); line-height: 1.2; }
  .service + .service { border-left: 1px solid #a8a8a8; }
  .service-immigration { width: 103px; }
  .service-education { width: 102px; }
  .service-accommodation { flex: 1; }
  .service-accommodation .label { text-align: center; }

  .site-footer { position: absolute; left: 0; top: 448px; width: 1200px; border-top: 1px solid var(--rule); }
  .footer-nav { position: absolute; top: 14px; left: 297px; font-size: 8px; font-weight: 500; }
  .footer-nav a { position: absolute; color: var(--ink); text-decoration: none; white-space: nowrap; }
  .copyright { position: absolute; top: 14px; right: 290px; font-size: 8px; white-space: nowrap; }
</style>
</head>
<body>
  <header class="site-header">
    <div class="brand"><span class="brand-name">OTV</span><span class="brand-mark"></span></div>
    <nav class="main-nav">
      <a class="nav-home" href="#" aria-label="Home">
        <svg width="12" height="12" viewBox="0 0 12 12"><path d="M1 6 L6 1.5 L11 6 H9.5 V11 H7 V8 H5 V11 H2.5 V6 Z" fill="#9a9a9a"/></svg>
      </a>
      <a class="nav-about" href="#">About Us</a>
      <a class="nav-services" href="#">Services
        <svg width="5" height="3" viewBox="0 0 5 3"><path d="M0.5 0.5 L2.5 2.5 L4.5 0.5" stroke="#e01b1b" fill="none"/></svg>
      </a>
      <a class="nav-contact" href="#">Contact</a>
    </nav>
    <div class="social"><span>Chirper</span><span class="sep"></span><span>Nodbook</span></div>
  </header>

  <section class="hero" role="img" aria-label="Photograph of a city skyline at dusk reflected in a river, with a bridge on the right"></section>

  <h1 class="tagline"><span class="line-one">Dare to</span><span class="line-two">Dream Canadian...</span></h1>

  <nav class="service-bar">
    <a class="service service-immigration">
      <svg width="20" height="24" viewBox="0 0 20 24"><rect x="1.5" y="1.5" width="17" height="21" fill="none" stroke="#1c1c1c" stroke-width="2"/><rect x="4" y="4" width="12" height="16" fill="#1c1c1c"/><rect x="6" y="15" width="8" height="1.5" fill="#dcdcdc"/></svg>
      <span class="label">Immigration</span>
    </a>
    <a class="service service-education">
      <svg width="30" height="22" viewBox="0 0 30 22"><path d="M15 2 L29 9 L15 16 L1 9 Z" fill="#1c1c1c"/><path d="M7 12 V18 Q15 22 23 18 V12 L15 16 Z" fill="#1c1c1c"/></svg>
      <span class="label">Education</span>
    </a>
    <a class="service service-accommodation">
      <svg width="26" height="24" viewBox="0 0 26 24"><path d="M13 1 L25 12 H21 V23 H5 V12 H1 Z" fill="#1c1c1c"/><path d="M13 19 L9.5 15.5 A2 2 0 0 1 13 13 A2 2 0 0 1 16.5 15.5 Z" fill="#ffffff"/></svg>
      <span class="label">Student Accommodation<br>Services</span>
    </a>
  </nav>

  <footer class="site-footer">
    <nav class="footer-nav">
      <a href="#" style="left:0">Home</a>
      <a href="#" style="left:41px">About Us</a>
      <a href="#" style="left:95px">Services</a>
      <a href="#" style="left:145px">Contact</a>
    </nav>
    <p class="copyright">2013 Northgatepartners. All rights reserved.</p>
  </footer>
</body>
</html>
```